Brambleton Enterprise Asset Management

I need a full website built that must work on destkop and mobile. I have the logo's and will upload them however some stock industrial photos will be required. I will be hosting it on wix/godaddy for use with dynamics 365. Pretty simple requirements:

*Splash page
*What We Do
*How We do it
*Who Are We?
*Software
*Partnerships
*Contact: Includes twitter/insta and email/addy/phone

The site should be more scroll oriented with fewer tabs to allow for a improved mobile experience.
We're also looking for ways to improve our inbound marketing and would want to include various areas to get in touch /or collect their info. Look to www.tallimor.com as an example of inbound marketing.
Images should be representative of the verticals we're focused on.

I have most of the content.

Asset intensive industries: Mining, Oil and Gas, Forest Products and Manufacturing.

Asset Management

Coded - Design and coding required

5+ page

Sans Serif

• Must be easy to view and navigate on mobile and desktop.
• Employee/Customer portal.
• Anything that will not display well in a mobile environment.

```html
<!DOCTYPE html>
<html lang="en">
<head>
<meta charset="utf-8">
<title>Brambleton EAM</title>
<link rel="stylesheet" href="https://fonts.googleapis.com/css2?family=Open+Sans:wght@400;600;700&display=swap">
<style>
:root{
  --navy:#1f4e6e;
  --olive:#9a9d62;
  --text:#555;
  --grey-bg:#f6f6f6;
  --logo-grey:#c4c4c4;
  --white:#fff;
}
*{box-sizing:border-box;margin:0;padding:0}
html,body{width:1200px;height:2679px;overflow:hidden}
body{font-family:"Open Sans",Arial,sans-serif;color:var(--text);background:var(--white);position:relative}
.abs{position:absolute}
section,header,footer{position:absolute;left:0;width:1200px}

/* header */
.site-header{top:0;height:110px;background:var(--white)}
.brand{left:75px;top:24px}
.brand-name{font-size:35px;font-weight:400;color:var(--navy);letter-spacing:1px;line-height:1}
.brand-rule{width:330px;height:2px;background:var(--navy);margin:6px 0 5px}
.brand-tag{font-size:16px;color:var(--navy);padding-left:72px}
.main-nav a{position:absolute;top:52px;font-size:14px;font-weight:600;color:#333;text-decoration:none}
.main-nav a.active{color:var(--olive)}

/* hero */
.hero{top:110px;height:536px;background:linear-gradient(135deg,#9aa4ad 0%,#c9ced3 35%,#7f8a95 65%,#4e5862 100%)}
.hero-shade{inset:0;background:rgba(20,30,40,.25)}
.hero h1{top:158px;width:1200px;text-align:center;font-size:50px;font-weight:700;color:var(--white)}
.hero p{top:232px;left:162px;width:876px;text-align:center;font-size:21.5px;line-height:36px;color:var(--white)}

/* section dots */
.dots{left:1115px;width:14px}
.dots span{display:block;width:14px;height:14px;border:2px solid var(--olive);border-radius:50%;margin-bottom:13px}
.dots span.on{border-color:var(--navy)}
.hero .dots span{border-color:var(--white)}
.hero .dots span.on{border-color:var(--navy)}

h2.section-title{position:absolute;font-size:32px;font-weight:600;color:var(--navy)}
h2.section-title em{font-style:normal;color:var(--olive)}

.ticks{list-style:none;position:absolute}
.ticks li{position:relative;padding-left:28px;color:var(--text);white-space:nowrap}
.ticks li svg{position:absolute;left:0;top:50%;transform:translateY(-50%)}

.btn{position:absolute;width:156px;height:43px;background:var(--olive);color:var(--white);font-size:15px;font-weight:600;text-align:center;line-height:43px}

.art{position:absolute;border-radius:6px}

/* business */
.business{top:646px;height:476px}
.business .ticks li{font-size:17px;height:43px;line-height:43px}
/* employee */
.employee{top:1122px;height:453px;background:var(--grey-bg)}
.sub-title{position:absolute;font-size:17px;font-weight:600;color:var(--navy)}
.employee .ticks li,.approach .ticks li{font-size:15px;height:32px;line-height:32px}
/* approach */
.approach{top:1575px;height:397px}
/* partners */
.partners{top:1972px;height:260px;background:var(--grey-bg)}
.partner-badge{position:absolute;top:2px;height:66px;background:var(--logo-grey);border-radius:8px;opacity:.8}
/* contact */
.contact{top:2232px;height:250px}
.contact p{position:absolute;width:1200px;text-align:center;font-size:18px;color:var(--text)}
/* footer */
.site-footer{top:2482px;height:197px;background:var(--grey-bg)}
.copyright{position:absolute;top:62px;width:1200px;text-align:center;font-size:13px;color:var(--olive)}
.social{position:absolute;top:106px;left:506px}
.social span{display:inline-block;width:25px;height:25px;background:#666;border-radius:4px;margin-right:14px}
</style>
</head>
<body>

<svg width="0" height="0" style="position:absolute">
  <defs>
    <symbol id="tick" viewBox="0 0 16 16"><circle cx="8" cy="8" r="8" fill="currentColor"/><path d="M4.3 8.2l2.5 2.5 5-5" stroke="#fff" stroke-width="2" fill="none"/></symbol>
  </defs>
</svg>

<header class="site-header">
  <div class="abs brand">
    <div class="brand-name">BRAMBLETON eam</div>
    <div class="brand-rule"></div>
    <div class="brand-tag">achieve greater results</div>
  </div>
  <nav class="main-nav">
    <a class="active" style="left:464px">Home</a>
    <a style="left:532px">What We Do</a>
    <a style="left:643px">How We Do It</a>
    <a style="left:761px">Who Are We?</a>
    <a style="left:875px">Software</a>
    <a style="left:963px">Partnerships</a>
    <a style="left:1075px">Contact</a>
  </nav>
</header>

<section class="hero" role="img" aria-label="Photo of hands reviewing printed business charts with a pen beside a keyboard">
  <div class="abs hero-shade"></div>
  <h1 class="abs">What is Brambleton EAM</h1>
  <p class="abs">Brambleton enterprise asset management is a boutique firm specializing in maintenance and reliability, supply chain, business intelligence and program management for asset intensive industries. We represent the finest people, process and technology tools to achieve greater results.</p>
  <div class="abs dots" style="top:190px"><span class="on"></span><span></span><span></span><span></span><span></span><span></span></div>
</section>

<section class="business">
  <div class="art" style="left:134px;top:86px;width:321px;height:322px;background:radial-gradient(circle at 50% 50%,#2a8fb0 0%,#6db6cc 40%,#ffffff 75%)" role="img" aria-label="Illustration of two businessmen shaking hands in front of a screen with speech bubbles"></div>
  <h2 class="section-title" style="left:564px;top:70px">Why <em>Business Drivers</em></h2>
  <ul class="ticks" style="left:564px;top:137px;color:var(--navy)">
    <li><svg width="16" height="16" style="color:#1f4e6e"><use href="#tick"/></svg>Improved planned &amp; scheduled maintenance</li>
    <li><svg width="16" height="16" style="color:#1f4e6e"><use href="#tick"/></svg>Uptime improvements</li>
    <li><svg width="16" height="16" style="color:#1f4e6e"><use href="#tick"/></svg>Longevity and safety of equipment</li>
    <li><svg width="16" height="16" style="color:#1f4e6e"><use href="#tick"/></svg>Optimized asset performance</li>
    <li><svg width="16" height="16" style="color:#1f4e6e"><use href="#tick"/></svg>Administrative savings</li>
  </ul>
  <div class="btn" style="left:564px;top:386px">Read More</div>
  <div class="abs dots" style="top:160px"><span></span><span class="on"></span><span></span><span></span><span></span><span></span></div>
</section>

<section class="employee">
  <h2 class="section-title" style="left:75px;top:45px">Why <em>Employee Drivers</em></h2>
  <div class="sub-title" style="left:75px;top:118px">Executive &amp; Operations Managers</div>
  <ul class="ticks" style="left:75px;top:146px">
    <li><svg width="14" height="14" style="color:#444"><use href="#tick"/></svg>More reliable operations</li>
    <li><svg width="14" height="14" style="color:#444"><use href="#tick"/></svg>Increased efficiency and profitability</li>
  </ul>
  <div class="sub-title" style="left:75px;top:225px">Maintenance Managers</div>
  <ul class="ticks" style="left:75px;top:253px">
    <li><svg width="14" height="14" style="color:#444"><use href="#tick"/></svg>Better information</li>
    <li><svg width="14" height="14" style="color:#444"><use href="#tick"/></svg>Identify where to spend money most effectively</li>
  </ul>
  <div class="sub-title" style="left:413px;top:118px">Maintenance Workers</div>
  <ul class="ticks" style="left:413px;top:146px">
    <li><svg width="14" height="14" style="color:#444"><use href="#tick"/></svg>Easier to prevent messes before they happen.</li>
    <li><svg width="14" height="14" style="color:#444"><use href="#tick"/></svg>Get information, not the runaround</li>
  </ul>
  <div class="art" style="left:800px;top:119px;width:298px;height:206px;background:linear-gradient(90deg,#f6f6f6 0%,#d9534f 30%,#c62828 75%,#f6f6f6 100%);opacity:.85" role="img" aria-label="Illustration of office workers carrying blocks to build a rising red bar chart"></div>
  <div class="btn" style="left:75px;top:360px">Read More</div>
  <div class="abs dots" style="top:150px"><span></span><span></span><span class="on"></span><span></span><span></span><span></span></div>
</section>

<section class="approach">
  <h2 class="section-title" style="left:0;width:1200px;text-align:center;top:34px">Why <em>Project Approach</em></h2>
  <div class="sub-title" style="left:164px;top:104px">Three Pillars</div>
  <ul class="ticks" style="left:164px;top:131px">
    <li><svg width="14" height="14" style="color:#444"><use href="#tick"/></svg>Maintenance &amp; Reliability</li>
    <li><svg width="14" height="14" style="color:#444"><use href="#tick"/></svg>Inventory &amp; Stores</li>
    <li><svg width="14" height="14" style="color:#444"><use href="#tick"/></svg>Procurement &amp; Payables</li>
  </ul>
  <div class="sub-title" style="left:527px;top:104px">Three Phases</div>
  <ul class="ticks" style="left:527px;top:131px">
    <li><svg width="14" height="14" style="color:#444"><use href="#tick"/></svg>Pre-Feasibility</li>
    <li><svg width="14" height="14" style="color:#444"><use href="#tick"/></svg>Feasibility</li>
    <li><svg width="14" height="14" style="color:#444"><use href="#tick"/></svg>Execution</li>
  </ul>
  <div class="sub-title" style="left:886px;top:104px">Three Dimensions</div>
  <ul class="ticks" style="left:886px;top:131px">
    <li><svg width="14" height="14" style="color:#444"><use href="#tick"/></svg>People &amp; Process</li>
    <li><svg width="14" height="14" style="color:#444"><use href="#tick"/></svg>Physical</li>
    <li><svg width="14" height="14" style="color:#444"><use href="#tick"/></svg>Technical</li>
  </ul>
  <div class="btn" style="left:522px;top:291px">Read More</div>
  <div class="abs dots" style="top:116px"><span></span><span></span><span></span><span class="on"></span><span></span><span></span></div>
</section>

<section class="partners">
  <h2 class="section-title" style="left:0;width:1200px;text-align:center;top:30px">Our <em>Partnerships</em></h2>
  <div class="abs" style="top:107px;left:0;width:1200px;height:72px">
    <div class="partner-badge" style="left:75px;width:230px;height:40px;top:16px"></div>
    <div class="partner-badge" style="left:361px;width:114px;border-radius:50%"></div>
    <div class="partner-badge" style="left:522px;width:250px;height:34px;top:19px"></div>
    <div class="partner-badge" style="left:830px;width:80px"></div>
    <div class="partner-badge" style="left:964px;width:102px"></div>
  </div>
  <div class="abs dots" style="top:51px"><span></span><span></span><span></span><span></span><span class="on"></span><span></span></div>
</section>

<section class="contact">
  <h2 class="section-title" style="left:0;width:1200px;text-align:center;top:42px">Contact <em>Us</em></h2>
  <p style="top:114px">42 Fenwick Lane, Carrow, K17 3PL</p>
  <p style="top:157px">
    <svg width="16" height="16" viewBox="0 0 16 16" style="vertical-align:-2px;margin-right:6px"><rect width="16" height="16" rx="3" fill="#9a9d62"/><path d="M5 3.5l2 2-1 1.3c.6 1.4 1.6 2.4 3 3l1.3-1 2 2-1.2 1.7C7.6 12.3 3.7 8.4 3.5 4.7z" fill="#fff"/></svg>604.555.0142
    <svg width="18" height="14" viewBox="0 0 18 14" style="vertical-align:-1px;margin:0 6px 0 20px"><rect width="18" height="14" rx="2" fill="#9a9d62"/><path d="M1.5 2l7.5 6 7.5-6" stroke="#fff" stroke-width="1.6" fill="none"/></svg>info@brambletonglobal.com
  </p>
  <div class="abs dots" style="top:44px"><span></span><span></span><span></span><span></span><span></span><span class="on"></span></div>
</section>

<footer class="site-footer">
  <div class="copyright">Copyright © 2016. Company Name. All Right Reserved</div>
  <div class="social"><span></span><span></span><span></span><span></span><span></span></div>
</footer>

</body>
</html>
```